Whitcombe Framing Works - Card Design

I am looking to use the logo designs that you already did for me to develop a business card. I would like the card to have a black background and be double sided. I want white and green logo and text. I have attached an inspiration photo of a look that I like. I would like to use the Vertical Logo attached to take up the full front side of the card. On the back where I have my name and information, I would like to have the horizontal logo or maybe even just the image of the 'A' and trees without the text. I am open, but I am looking for something clean and simple and I want the green to really pop! Additional files can be found under Design #: 40593216

Target Market(s)

Homeowners

Industry/Entity Type

Construction

Contact Information for Business Card

Name: Marcus Pellow, Title: Project Manager, Phone: 831.555.0147, Email: whitcombeframingworks@mailbarn.net, address: 418 Juniper Ln, Felton, CA 95092, Lic# 2046318

Colors
00AB8E
00BBA5
67D7C9
C6EFE9
E9F9F6

Requirements
Nice to have
• I would like to see the logos that I have already got from SketchHarbor, though I am open to new ones

```html
<!DOCTYPE html>
<html lang="en">
<head>
<meta charset="utf-8">
<title>Whitcombe Framing Works – Business Card</title>
<link href="https://fonts.googleapis.com/css2?family=Lato:wght@400;700;900&display=swap" rel="stylesheet">
<style>
  :root {
    --ink: #231f20;
    --green: #62b540;
    --white: #ffffff;
    --paper: #e6e4e1;
    --text-dark: #2a2a2a;
  }
  * { box-sizing: border-box; margin: 0; padding: 0; }
  html, body { width: 1200px; height: 977px; overflow: hidden; }
  body {
    background: var(--paper);
    font-family: "Lato", sans-serif;
    position: relative;
  }
  .card {
    position: absolute;
    left: 250px;
    width: 700px;
    height: 400px;
    border-radius: 22px;
    overflow: hidden;
  }
  .card--front { top: 50px; background: var(--ink); }
  .card--back { top: 520px; background: var(--white); }

  /* Front */
  .front-brand {
    position: absolute;
    left: 0; right: 0; top: 92px;
    display: flex; flex-direction: column; align-items: center;
  }
  .brand-mark {
    width: 54px; height: 54px;
    background: var(--green);
    margin-bottom: 26px;
  }
  .brand-name {
    color: var(--white);
    font-weight: 900;
    text-transform: uppercase;
    text-align: center;
    letter-spacing: 3px;
    line-height: 1.1;
  }
  .brand-name--front { font-size: 44px; }
  .estd {
    position: absolute;
    top: 118px;
    color: var(--white);
    font-size: 15px;
    letter-spacing: 4px;
    padding: 6px 4px;
    border-top: 1.5px solid var(--green);
    border-bottom: 1.5px solid var(--green);
  }
  .estd--label { left: 70px; }
  .estd--year { right: 70px; }

  /* Back */
  .back-bg { position: absolute; inset: 0; }
  .back-brand {
    position: absolute;
    left: 0; right: 0; top: 52px;
    display: flex; align-items: center; justify-content: center; gap: 18px;
  }
  .back-brand .brand-mark { width: 40px; height: 40px; margin: 0; }
  .brand-name--back { font-size: 28px; letter-spacing: 2px; }

  .person {
    position: absolute;
    left: 30px; width: 320px; top: 292px;
    text-align: right;
  }
  .person-name {
    color: var(--green);
    font-weight: 900;
    font-size: 31px;
    text-transform: uppercase;
    letter-spacing: 0.5px;
  }
  .person-title {
    color: var(--text-dark);
    font-size: 19px;
    margin-top: 2px;
  }
  .divider {
    position: absolute;
    left: 372px; top: 236px;
    width: 1.5px; height: 140px;
    background: var(--green);
  }
  .contacts {
    position: absolute;
    left: 392px; top: 236px;
    list-style: none;
    color: var(--text-dark);
    font-size: 15px;
    line-height: 1.35;
  }
  .contacts li { display: flex; align-items: flex-start; gap: 9px; margin-bottom: 5px; }
  .contacts svg { flex: none; width: 13px; height: 13px; margin-top: 3px; fill: var(--green); }
  .contacts .no-icon { padding-left: 22px; }
</style>
</head>
<body>

<section class="card card--front" aria-label="Card front">
  <span class="estd estd--label">ESTD</span>
  <span class="estd estd--year">2020</span>
  <div class="front-brand">
    <span class="brand-mark" aria-hidden="true"></span>
    <p class="brand-name brand-name--front">Whitcombe<br>Framing Works</p>
  </div>
</section>

<section class="card card--back" aria-label="Card back">
  <svg class="back-bg" viewBox="0 0 700 400" preserveAspectRatio="none" aria-hidden="true">
    <polygon points="0,0 700,0 700,170 0,270" fill="var(--ink)"/>
    <line x1="0" y1="272" x2="700" y2="172" stroke="var(--green)" stroke-width="4"/>
  </svg>

  <div class="back-brand">
    <span class="brand-mark" aria-hidden="true"></span>
    <p class="brand-name brand-name--back">Whitcombe Framing Works</p>
  </div>

  <div class="person">
    <p class="person-name">Marcus Pellow</p>
    <p class="person-title">Project Manager</p>
  </div>

  <span class="divider" aria-hidden="true"></span>

  <ul class="contacts">
    <li>
      <svg viewBox="0 0 24 24" aria-hidden="true"><path d="M12 1a8 8 0 0 0-8 8c0 6 8 14 8 14s8-8 8-14a8 8 0 0 0-8-8zm0 11a3 3 0 1 1 0-6 3 3 0 0 1 0 6z"/></svg>
      <span>418 Juniper Ln<br>Felton, CA 95092</span>
    </li>
    <li>
      <svg viewBox="0 0 24 24" aria-hidden="true"><path d="M6.6 10.8a15 15 0 0 0 6.6 6.6l2.2-2.2a1 1 0 0 1 1-.25 11.4 11.4 0 0 0 3.6.6 1 1 0 0 1 1 1V20a1 1 0 0 1-1 1A17 17 0 0 1 3 4a1 1 0 0 1 1-1h3.5a1 1 0 0 1 1 1c0 1.25.2 2.45.6 3.6a1 1 0 0 1-.25 1z"/></svg>
      <span>831.555.0147</span>
    </li>
    <li>
      <svg viewBox="0 0 24 24" aria-hidden="true"><path d="M2 5h20v14H2zm2 2v.5l8 5 8-5V7l-8 5z"/></svg>
      <span>whitcombeframingworks@mailbarn.net</span>
    </li>
    <li class="no-icon"><span>Lic# 2046318</span></li>
  </ul>
</section>

</body>
</html>
```